i would like a business card to leave with customers and potential customers for electrical work and for the supply and install of reverse cycle airconditioning in the domestic and commercial market.
I own my own business and im a sole trader. I have an a'class electrical lisence and also a refrigeration lisence so i am
able to offer complete installations in airconditioning by a fully qualified and lisenced tradesman.
im looking for something that comes across as unique and professional.
i had the coluor black and some gold in mind but open to any coluors.
something like Beacon Electrical & Refrigeration
or Beacon Air.
i will use this design on a business card to advertise through summer to help generate installs through the busy season.

Target Market(s)

Mainly domestic house holds through summer who are in need of airconditioning and reliable information to acomadate thier cooling and heating requirements

Industry/Entity Type

Electrical

Requirements
Must have
• Business name- Beacon
My name- Peter Wollaston
My mobile no- 0457 819 302
My email- prwollaston@tarvel.com.au
Installation & Decomissioning of aiconditioning split systems
LIC NO: KTR 407516
Nice to have
• Beacon Electrical & Refrigeration

```html
<!DOCTYPE html>
<html lang="en">
<head>
<meta charset="utf-8">
<title>Beacon Electrical &amp; Refrigeration — Business Card</title>
<link rel="stylesheet" href="https://fonts.googleapis.com/css2?family=PT+Sans:wght@400;700&display=swap">
<style>
  :root {
    --page: #222426;
    --card-dark: #263034;
    --card-mid: #3d4a4f;
    --card-light: #b3c3c3;
    --text: #ffffff;
    --text-soft: #c9d2d4;
    --rule: #d9e6e8;
    --dots: #8e9ea2;
  }
  * { margin: 0; padding: 0; box-sizing: border-box; }
  html, body {
    width: 1200px; height: 1198px; overflow: hidden;
    background: var(--page);
    font-family: "PT Sans", "Myriad Pro", Arial, sans-serif;
    color: var(--text);
  }
  .canvas { position: relative; width: 1200px; height: 1198px; }

  .card { position: absolute; overflow: hidden; }
  .card--front {
    left: 80px; top: 138px; width: 705px; height: 438px;
    background:
      radial-gradient(ellipse 520px 420px at 100% 0%, var(--card-light) 0%, var(--card-mid) 45%, transparent 80%),
      linear-gradient(180deg, var(--card-mid) 0%, var(--card-dark) 100%);
  }
  .card--back {
    left: 411px; top: 613px; width: 709px; height: 441px;
    background:
      radial-gradient(ellipse 520px 420px at 0% 0%, var(--card-light) 0%, var(--card-mid) 45%, transparent 80%),
      linear-gradient(180deg, var(--card-mid) 0%, var(--card-dark) 100%);
  }

  .rule { position: absolute; height: 3px; }
  .rule--fade-right { background: linear-gradient(90deg, var(--rule) 0%, var(--rule) 55%, transparent 100%); }
  .rule--fade-left { background: linear-gradient(90deg, transparent 0%, var(--rule) 40%, var(--rule) 100%); }

  .halftone { position: absolute; }
  .halftone--front {
    left: 6px; top: 142px; width: 366px; height: 188px;
    background: linear-gradient(90deg, rgba(142,158,162,0.55) 0%, rgba(142,158,162,0.35) 60%, transparent 100%);
  }
  .halftone--back {
    left: 341px; top: 101px; width: 359px; height: 189px;
    background: linear-gradient(90deg, transparent 0%, rgba(142,158,162,0.35) 40%, rgba(142,158,162,0.55) 100%);
  }

  .company {
    position: absolute; left: 27px; top: 82px;
    font-size: 26px; font-weight: 700; letter-spacing: 0.2px;
  }
  .person { position: absolute; right: 43px; top: 272px; text-align: right; }
  .person__name { font-size: 35px; font-weight: 700; line-height: 1; }
  .person__role { font-size: 19px; color: var(--text-soft); margin-top: 2px; }

  .contacts {
    position: absolute; left: 26px; top: 132px;
    list-style: none; font-size: 21px; line-height: 30px; color: var(--text);
  }
  .socials {
    position: absolute; left: 0; right: 0; top: 324px;
    display: flex; justify-content: center; gap: 14px;
    font-size: 13px; color: var(--text-soft);
  }
  .socials__item { display: flex; align-items: center; gap: 5px; }
  .socials__mark { width: 12px; height: 12px; background: #5f8fb8; }
  .services {
    position: absolute; left: 0; right: 0; top: 372px;
    text-align: center; font-size: 17px; line-height: 22px; color: var(--text);
  }
</style>
</head>
<body>
<main class="canvas">

  <section class="card card--front" aria-label="Card front">
    <h1 class="company">Beacon Electrical &amp; Refrigeration</h1>
    <div class="rule rule--fade-right" style="left:0; top:136px; width:400px;"></div>
    <div class="halftone halftone--front" role="img" aria-label="Halftone square dot pattern"></div>
    <div class="rule rule--fade-left" style="left:90px; top:331px; width:300px;"></div>
    <div class="person">
      <div class="person__name">Peter Wollaston</div>
      <div class="person__role">CEO</div>
    </div>
  </section>

  <section class="card card--back" aria-label="Card back">
    <div class="rule rule--fade-left" style="left:298px; top:97px; width:411px;"></div>
    <div class="halftone halftone--back" role="img" aria-label="Halftone square dot pattern"></div>
    <div class="rule rule--fade-left" style="left:330px; top:296px; width:379px;"></div>
    <ul class="contacts">
      <li>0457 819 302</li>
      <li>prwollaston@tarvel.com.au</li>
      <li>chirpline.com/peter</li>
      <li>facepage.com/peter</li>
      <li>linkup.com/in/peter</li>
    </ul>
    <div class="socials">
      <span class="socials__item"><span class="socials__mark"></span>Facepage</span>
      <span class="socials__item"><span class="socials__mark"></span>Chirpline</span>
      <span class="socials__item"><span class="socials__mark"></span>Blogr</span>
      <span class="socials__item"><span class="socials__mark"></span>Linkup</span>
    </div>
    <p class="services">Installation &amp; Decomissioning of aiconditioning split systems<br>LIC NO: KTR 407516</p>
  </section>

</main>
</body>
</html>
```